Heron Freightlines needs Bussiness cards!

Our new trucking company needs business cards!
We need the same design with two different names and emails, everything else it's the same.
I have included our original logo so we can use it for the design.
Note: the logo to be used is the o e with the buffalo on the right side, next to the letters H and F.

Target Market(s)

Trucking, refrigerated transportation, freight

Industry/Entity Type

Business

Contact Information for Business Card

Card #1:
Marcus Tellwright
marcustellwright@heronfreightlines.example
1-844-555-0193
(956)555-0178
3817 W. Tarrow Ave.
Pharr, TX 78599
www.heronfreightlines.example

Card#2:
Orla Brennick
orla@heronfreightlines.example
1-844-555-0193
(956)555-0178
3817 W. Tarrow Ave.
Pharr, TX 78599
www.heronfreightlines.example

Font styles to use
Sans Serif

Colors
0655a3
ec1f27
ffffff

Requirements
Must have
• our logo
Nice to have
• roads on background,

```html
<!DOCTYPE html>
<html lang="en">
<head>
<meta charset="utf-8">
<title>Heron Freightlines – Business Cards</title>
<link rel="stylesheet" href="https://fonts.googleapis.com/css2?family=Roboto:wght@400;500;700&display=swap">
<style>
  :root {
    --navy: #0f2f5c;
    --blue: #0655a3;
    --red: #c8161f;
    --white: #ffffff;
    --paper: #e9e6e1;
    --ink: #222a33;
    --road-dark: #1c2c3e;
    --road-mid: #3a4d5e;
  }
  * { margin: 0; padding: 0; box-sizing: border-box; }
  html, body { width: 1200px; height: 913px; overflow: hidden; }
  body {
    background: var(--paper);
    font-family: "Roboto", Arial, sans-serif;
    position: relative;
  }
  .card {
    position: absolute;
    width: 540px;
    height: 308px;
    background: var(--white);
    overflow: hidden;
    box-shadow: 0 6px 18px rgba(0,0,0,.18);
  }
  .card--front { left: 40px; top: 60px; }
  .card--marcus { left: 620px; top: 60px; }
  .card--orla { left: 330px; top: 530px; }

  /* front */
  .front-art { position: absolute; inset: 0; }
  .brand {
    position: absolute;
    left: 48px;
    top: 100px;
    display: flex;
    align-items: center;
    gap: 10px;
    color: var(--navy);
    font-weight: 700;
    font-size: 28px;
  }
  .brand__dot {
    width: 18px; height: 18px;
    border-radius: 50%;
    background: var(--red);
  }

  /* back */
  .back-brand {
    position: absolute;
    left: 30px;
    top: 206px;
    color: var(--navy);
    font-weight: 700;
    font-size: 18px;
  }
  .contact {
    position: absolute;
    left: 236px;
    top: 48px;
    width: 280px;
    color: var(--ink);
  }
  .contact__name {
    color: var(--red);
    font-size: 23px;
    font-weight: 400;
    margin-bottom: 8px;
  }
  .contact__list { list-style: none; }
  .contact__item {
    display: flex;
    align-items: center;
    gap: 8px;
    font-size: 11.5px;
    line-height: 20px;
    white-space: nowrap;
  }
  .icon { width: 13px; height: 13px; flex: none; }
  .contact__rule {
    height: 2px;
    background: var(--red);
    margin: 12px 0 10px;
    width: 280px;
  }
  .address {
    display: flex;
    gap: 8px;
    font-size: 11.5px;
    line-height: 17px;
  }
  .address .icon { margin-top: 2px; }
</style>
</head>
<body>

<section class="card card--front" aria-label="Card front">
  <svg class="front-art" viewBox="0 0 540 308" width="540" height="308">
    <defs>
      <linearGradient id="roadPhoto" x1="0" y1="1" x2="1" y2="0">
        <stop offset="0" stop-color="var(--road-dark)"/>
        <stop offset=".6" stop-color="var(--road-mid)"/>
        <stop offset="1" stop-color="#8ea0b0"/>
      </linearGradient>
    </defs>
    <polygon points="540,60 540,308 95,308" fill="url(#roadPhoto)"
             role="img" aria-label="Photograph of a mountain highway stretching into the distance"/>
    <line x1="540" y1="60" x2="95" y2="308" stroke="var(--red)" stroke-width="5"/>
  </svg>
  <div class="brand"><span class="brand__dot"></span>Heron Freightlines</div>
</section>

<section class="card card--marcus" aria-label="Card back, Marcus Tellwright">
  <div class="back-brand">Heron Freightlines</div>
  <div class="contact">
    <h1 class="contact__name">Marcus Tellwright</h1>
    <ul class="contact__list">
      <li class="contact__item">
        <svg class="icon" viewBox="0 0 14 14"><circle cx="7" cy="7" r="7" fill="var(--red)"/><path d="M4.5 3.5l1.5 0 .7 2-1 .8a5 5 0 0 0 2 2l.8-1 2 .7 0 1.5c-3.5.5-6.5-2.5-6-6z" fill="#fff"/></svg>
        1-844-555-0193
      </li>
      <li class="contact__item">
        <svg class="icon" viewBox="0 0 14 14"><circle cx="7" cy="7" r="7" fill="var(--red)"/><rect x="5" y="3" width="4" height="8" rx=".8" fill="none" stroke="#fff" stroke-width="1.1"/></svg>
        (956)555-0178
      </li>
      <li class="contact__item">
        <svg class="icon" viewBox="0 0 14 14"><circle cx="7" cy="7" r="7" fill="var(--red)"/><rect x="3.5" y="4.5" width="7" height="5" fill="none" stroke="#fff" stroke-width="1"/><path d="M3.5 4.5l3.5 3 3.5-3" fill="none" stroke="#fff" stroke-width="1"/></svg>
        marcustellwright@heronfreightlines.example
      </li>
      <li class="contact__item">
        <svg class="icon" viewBox="0 0 14 14"><circle cx="7" cy="7" r="7" fill="var(--red)"/><circle cx="7" cy="7" r="3.6" fill="none" stroke="#fff" stroke-width="1"/><path d="M3.4 7h7.2M7 3.4c-1.6 2-1.6 5.2 0 7.2M7 3.4c1.6 2 1.6 5.2 0 7.2" fill="none" stroke="#fff" stroke-width=".8"/></svg>
        www.heronfreightlines.example
      </li>
    </ul>
    <div class="contact__rule"></div>
    <div class="address">
      <svg class="icon" viewBox="0 0 14 14"><circle cx="7" cy="7" r="7" fill="var(--red)"/><path d="M3.5 7.2L7 4l3.5 3.2M4.6 6.4v3.6h4.8V6.4" fill="none" stroke="#fff" stroke-width="1.1"/></svg>
      <div>3817 W. Tarrow Ave.<br>Pharr, TX 78599</div>
    </div>
  </div>
</section>

<section class="card card--orla" aria-label="Card back, Orla Brennick">
  <div class="back-brand">Heron Freightlines</div>
  <div class="contact">
    <h1 class="contact__name">Orla Brennick</h1>
    <ul class="contact__list">
      <li class="contact__item">
        <svg class="icon" viewBox="0 0 14 14"><circle cx="7" cy="7" r="7" fill="var(--red)"/><path d="M4.5 3.5l1.5 0 .7 2-1 .8a5 5 0 0 0 2 2l.8-1 2 .7 0 1.5c-3.5.5-6.5-2.5-6-6z" fill="#fff"/></svg>
        1-844-555-0193
      </li>
      <li class="contact__item">
        <svg class="icon" viewBox="0 0 14 14"><circle cx="7" cy="7" r="7" fill="var(--red)"/><rect x="5" y="3" width="4" height="8" rx=".8" fill="none" stroke="#fff" stroke-width="1.1"/></svg>
        (956)555-0178
      </li>
      <li class="contact__item">
        <svg class="icon" viewBox="0 0 14 14"><circle cx="7" cy="7" r="7" fill="var(--red)"/><rect x="3.5" y="4.5" width="7" height="5" fill="none" stroke="#fff" stroke-width="1"/><path d="M3.5 4.5l3.5 3 3.5-3" fill="none" stroke="#fff" stroke-width="1"/></svg>
        orla@heronfreightlines.example
      </li>
      <li class="contact__item">
        <svg class="icon" viewBox="0 0 14 14"><circle cx="7" cy="7" r="7" fill="var(--red)"/><circle cx="7" cy="7" r="3.6" fill="none" stroke="#fff" stroke-width="1"/><path d="M3.4 7h7.2M7 3.4c-1.6 2-1.6 5.2 0 7.2M7 3.4c1.6 2 1.6 5.2 0 7.2" fill="none" stroke="#fff" stroke-width=".8"/></svg>
        www.heronfreightlines.example
      </li>
    </ul>
    <div class="contact__rule"></div>
    <div class="address">
      <svg class="icon" viewBox="0 0 14 14"><circle cx="7" cy="7" r="7" fill="var(--red)"/><path d="M3.5 7.2L7 4l3.5 3.2M4.6 6.4v3.6h4.8V6.4" fill="none" stroke="#fff" stroke-width="1.1"/></svg>
      <div>3817 W. Tarrow Ave.<br>Pharr, TX 78599</div>
    </div>
  </div>
</section>

</body>
</html>
```